Liquor Label / Aguardiente

Label design for liquor bottle. Designers may submit multiple submissions.

Product Description:
Name: Luna de Cobre™
Alcohol Category: Aguardiente (which in Spanish most closely translates to “burning water”) – aguardiente is derived from
cane sugar and is a general term for a type of alcoholic spirit in many Central and South America countries.
Taste: A smooth liquor with a comfortable yet spicy finish
Smell: Subtle aroma of spicy jalapeños
Liquid Color: Clear
Bottle Color: Clear
See link for reference - http://www.pellowinery.example/sites/default/files/styles/uc_product_full/public/Vessel_0.jpg?itok=8KqTm2Xw
Closure: Bar top / cork
Bottle Shape/Size: height = 8.67in; diameter of base = 3.70in; diameter of neck = 0.85in

Label may consist of two separate parts (i.e. front and back, front and vertical side), or one continuous label.

Designer has complete freedom with color, font etc. unless otherwise stated below. The label MUST
contain (but is not limited only to) the following text exactly as written in quotes below:
- “Luna de Cobre”
- “Aguardiente”
- “Cane Neutral Spirit with Natural Flavors”
- “35% Alc./Vol.”
- “750 ml”
- “Bottled by QM Spirits, LLC” and “Nashville, TN” - “Government Warning: (1) According to the Surgeon General, women should not drink alcoholic beverages during
pregnancy because of the risk of birth defects. (2) Consumption of alcoholic beverages impairs your ability to
drive a car or operate machinery, and may cause health problems.” (text in previous quotes must be in all
capitalized letters, text must be 2 MM in height and quote must be separated 2MM by all other text)
- Must be dedicated empty space for bar code (approximately 0.75in. height x 1.25in. length)
Updates

Target Market(s)

Label should have mass market appeal.
Age: 21 – 28 years old (primary target market is 21+ year old college students and recent graduates)
Target Market Gender: Both male and female, with emphasis on male
Consumption Focus: Spirit will be consumed typically as a shot, primarily at bars and secondarily off premise (label design will be critical for making our product highly visible behind a bar)
Marketing Theme: South American elements. The official Luna de Cobre mascot is a llama and the incorporation and use of a llama somewhere (however large or small) on the bottle is encourage but by no means required.

Industry/Entity Type

Health

Requirements
Should not have
• Elements that may lead a potential consumer to believe the beverage is a craft liquor or an artisan brand. Please do not include images of peppers.

```html
<!DOCTYPE html>
<html lang="en">
<head>
<meta charset="utf-8">
<title>Luna de Cobre – Aguardiente Label</title>
<link href="https://fonts.googleapis.com/css2?family=Oswald:wght@300;400;500&family=Roboto:wght@400;700&display=swap" rel="stylesheet">
<style>
  :root {
    --canvas-bg: #ececec;
    --ribbon-red: #e61d27;
    --ribbon-red-deep: #c3141c;
    --ribbon-fold: #8c0d13;
    --ribbon-tail: #b3121a;
    --white: #ffffff;
    --category-muted: #3b5f86;
    --category-bright: #1f6fc2;
    --sky: #3f8fd2;
    --haze: #eef5f2;
    --hills: #6d9c3c;
    --village: #d9d2c4;
    --terracotta: #b8643a;
    --band-black: #000000;
    --band-yellow: #fff200;
    --band-red-text: #c3141c;
    --barcode-edge: #9a9a9a;
  }
  * { box-sizing: border-box; margin: 0; padding: 0; }
  html, body { width: 1200px; height: 1060px; overflow: hidden; }
  body { background: var(--canvas-bg); font-family: "Roboto", Arial, sans-serif; }

  .canvas { position: relative; width: 1200px; height: 1060px; }

  .label { position: absolute; top: 165px; width: 560px; height: 700px; }
  .label--classic { left: 30px; }
  .label--bright { left: 610px; }

  .label__body {
    position: absolute; left: 52px; top: 140px; width: 456px; height: 550px;
    display: flex; flex-direction: column; overflow: hidden;
  }
  .label__scene {
    flex: 1;
    background: linear-gradient(180deg,
      var(--sky) 0%, #8fc1e6 18%, var(--haze) 34%,
      #a9c98a 44%, var(--hills) 56%, #4f7d2e 64%,
      var(--terracotta) 70%, var(--village) 78%, #f4f1ea 90%, #9a938a 100%);
  }
  .label__facts {
    flex: 0 0 auto; padding: 6px 10px 8px;
    font-family: "Oswald", "Arial Narrow", sans-serif; text-transform: uppercase;
  }
  .facts__main {
    font-size: 15px; font-weight: 500; line-height: 19px; text-align: center;
    white-space: nowrap; letter-spacing: 0.1px;
  }
  .facts__spirit { font-size: 11px; font-weight: 400; line-height: 15px; text-align: center; letter-spacing: 0.4px; }
  .facts__row { display: flex; align-items: center; gap: 10px; margin-top: 5px; }
  .facts__warning { flex: 1; font-size: 9.5px; font-weight: 300; line-height: 12px; text-align: center; }
  .facts__barcode { flex: 0 0 96px; height: 58px; background: var(--white); border: 1px solid var(--barcode-edge); }

  .label--classic .label__facts { background: var(--band-black); color: var(--white); }
  .label--bright .label__facts { background: var(--band-yellow); color: var(--band-red-text); }

  .label__category {
    position: absolute; top: 152px; left: 102px; width: 340px; height: 48px;
    display: flex; align-items: center; justify-content: center;
    color: var(--white); font-size: 36px; font-weight: 400; letter-spacing: 1px;
  }
  .label--classic .label__category { background: var(--category-muted); opacity: 0.92; }
  .label--bright .label__category { background: var(--category-bright); }

  .label__ribbon { position: absolute; left: 0; top: 0; width: 560px; height: 200px; }

  .label__name {
    position: absolute; left: 0; top: 6px; width: 560px; height: 140px;
    display: flex; flex-direction: column; align-items: center; justify-content: center;
    color: var(--white); font-family: "Roboto", Arial, sans-serif; font-weight: 700;
    text-transform: uppercase; line-height: 0.92;
  }
  .name__top { font-size: 58px; letter-spacing: 1px; }
  .name__bottom { font-size: 82px; letter-spacing: 1px; }
</style>
</head>
<body>
<main class="canvas">

  <section class="label label--classic">
    <div class="label__body">
      <div class="label__scene" role="img" aria-label="Photograph of a colonial village street with whitewashed houses and terracotta roofs beneath green hills and a bright blue sky"></div>
      <div class="label__facts">
        <p class="facts__main">35% Alc./Vol. 750 ml&nbsp; Bottled by QM Spirits, LLC Nashville, TN</p>
        <p class="facts__spirit">Cane Neutral Spirit with Natural Flavors</p>
        <div class="facts__row">
          <p class="facts__warning">Government Warning: (1) According to the Surgeon General, women should not drink alcoholic beverages during pregnancy because of the risk of birth defects. (2) Consumption of alcoholic beverages impairs your ability to drive a car or operate machinery, and may cause health problems.</p>
          <div class="facts__barcode" aria-label="Space reserved for barcode"></div>
        </div>
      </div>
    </div>
    <div class="label__category">AGUARDIENTE</div>
    <svg class="label__ribbon" viewBox="0 0 560 200" aria-hidden="true">
      <defs>
        <linearGradient id="ribbonShadeA" x1="0" x2="1" y1="0" y2="0">
          <stop offset="0" stop-color="var(--ribbon-red-deep)"/>
          <stop offset="0.2" stop-color="var(--ribbon-red)"/>
          <stop offset="0.8" stop-color="var(--ribbon-red)"/>
          <stop offset="1" stop-color="var(--ribbon-red-deep)"/>
        </linearGradient>
      </defs>
      <polygon points="52,138 52,196 4,186 24,166 8,146" fill="var(--ribbon-tail)"/>
      <polygon points="508,142 508,198 556,190 536,170 552,150" fill="var(--ribbon-tail)"/>
      <polygon points="22,142 52,142 52,170" fill="var(--ribbon-fold)"/>
      <polygon points="538,148 508,148 508,176" fill="var(--ribbon-fold)"/>
      <polygon points="8,0 552,6 552,150 8,142" fill="url(#ribbonShadeA)"/>
    </svg>
    <h1 class="label__name"><span class="name__top">Luna de</span><span class="name__bottom">Cobre</span></h1>
  </section>

  <section class="label label--bright">
    <div class="label__body">
      <div class="label__scene" role="img" aria-label="Photograph of a colonial village street with whitewashed houses and terracotta roofs beneath green hills and a bright blue sky"></div>
      <div class="label__facts">
        <p class="facts__main">35% Alc./Vol. 750 ml&nbsp; Bottled by QM Spirits, LLC Nashville, TN</p>
        <p class="facts__spirit">Cane Neutral Spirit with Natural Flavors</p>
        <div class="facts__row">
          <p class="facts__warning">Government Warning: (1) According to the Surgeon General, women should not drink alcoholic beverages during pregnancy because of the risk of birth defects. (2) Consumption of alcoholic beverages impairs your ability to drive a car or operate machinery, and may cause health problems.</p>
          <div class="facts__barcode" aria-label="Space reserved for barcode"></div>
        </div>
      </div>
    </div>
    <div class="label__category">AGUARDIENTE</div>
    <svg class="label__ribbon" viewBox="0 0 560 200" aria-hidden="true">
      <defs>
        <linearGradient id="ribbonShadeB" x1="0" x2="1" y1="0" y2="0">
          <stop offset="0" stop-color="var(--ribbon-red-deep)"/>
          <stop offset="0.2" stop-color="var(--ribbon-red)"/>
          <stop offset="0.8" stop-color="var(--ribbon-red)"/>
          <stop offset="1" stop-color="var(--ribbon-red-deep)"/>
        </linearGradient>
      </defs>
      <polygon points="52,138 52,196 4,186 24,166 8,146" fill="var(--ribbon-tail)"/>
      <polygon points="508,142 508,198 556,190 536,170 552,150" fill="var(--ribbon-tail)"/>
      <polygon points="22,142 52,142 52,170" fill="var(--ribbon-fold)"/>
      <polygon points="538,148 508,148 508,176" fill="var(--ribbon-fold)"/>
      <polygon points="8,0 552,6 552,150 8,142" fill="url(#ribbonShadeB)"/>
    </svg>
    <h1 class="label__name"><span class="name__top">Luna de</span><span class="name__bottom">Cobre</span></h1>
  </section>

</main>
</body>
</html>
```